Finance Product Agency Business Card Design

We're an agency that provides products (service contracts, gap insurance, tire and wheel, etc) and support to dealership finance departments. We specialize in training finance producers to maximize their potential and also keep them up to date on the ever changing compliance and legal landscape. I'll attach an image of our logo, excited to see what you all come up with. Would also be interested in discussing our new website design with the winner.

Target Market(s)

auto dealerships

Industry/Entity Type

Business

Contact Information for Business Card

Mark Dolvery
Phone 317.624.5583
Fax 855.472.3308
email Mark.Dolvery@brightlanecoverage.example

Requirements
Must have
• basic contact information
Nice to have
• looking for something professional but modern

```html
<!DOCTYPE html>
<html lang="en">
<head>
<meta charset="utf-8">
<title>Brightlane Coverage – Business Card</title>
<link rel="stylesheet" href="https://fonts.googleapis.com/css2?family=Roboto+Condensed:wght@400;700&display=swap">
<style>
  :root {
    --backdrop: #8e8e8e;
    --card: #e9e9eb;
    --ink-brand: #34505f;
    --ink-text: #2f3236;
    --band-start: #34505f;
    --band-end: #1b1e21;
  }
  * { margin: 0; padding: 0; box-sizing: border-box; }
  html, body {
    width: 1105px;
    height: 1200px;
    overflow: hidden;
  }
  body {
    position: relative;
    background: var(--backdrop);
    font-family: "Roboto Condensed", "Arial Narrow", sans-serif;
  }
  .card {
    position: absolute;
    left: 182px;
    width: 746px;
    height: 424px;
    background: var(--card);
  }
  .card--front { top: 119px; }
  .card--back { top: 636px; }

  .card__band {
    position: absolute;
    top: 0; left: 0; right: 0;
    height: 15px;
    background: linear-gradient(90deg, var(--band-start) 0%, var(--band-start) 45%, var(--band-end) 100%);
  }

  .brand-mark {
    position: absolute;
    left: 50%;
    top: 82px;
    transform: translateX(-50%);
    display: flex;
    flex-direction: column;
    align-items: center;
    gap: 10px;
  }
  .brand-mark__dot {
    width: 74px;
    height: 74px;
    border-radius: 50%;
    background: var(--ink-brand);
  }
  .brand-mark__name {
    font-weight: 700;
    font-size: 18px;
    letter-spacing: 1px;
    color: var(--ink-brand);
    white-space: nowrap;
  }

  .contact {
    position: absolute;
    left: 0; right: 0;
    top: 244px;
    text-align: center;
    color: var(--ink-text);
  }
  .contact__name {
    font-weight: 700;
    font-size: 28px;
    color: var(--ink-brand);
    margin-bottom: 10px;
  }
  .contact__line {
    font-size: 19px;
    line-height: 29px;
  }
  .contact__phones {
    display: flex;
    justify-content: center;
    align-items: center;
    gap: 8px;
    font-size: 20px;
  }
  .contact__phones svg {
    width: 18px;
    height: 18px;
    fill: var(--ink-text);
    margin-right: 3px;
    vertical-align: -2px;
  }

  .lockup {
    position: absolute;
    left: 180px;
    top: 168px;
    display: flex;
    align-items: center;
    gap: 20px;
  }
  .lockup__dot {
    width: 84px;
    height: 84px;
    border-radius: 50%;
    background: var(--ink-brand);
  }
  .lockup__name {
    font-weight: 700;
    font-size: 44px;
    color: var(--ink-brand);
    white-space: nowrap;
  }
</style>
</head>
<body>

  <section class="card card--front">
    <div class="card__band"></div>

    <div class="brand-mark">
      <div class="brand-mark__dot"></div>
      <div class="brand-mark__name">BRIGHTLANE COVERAGE</div>
    </div>

    <div class="contact">
      <h1 class="contact__name">Mark Dolvery</h1>
      <p class="contact__line contact__phones">
        <span>
          <svg viewBox="0 0 24 24" aria-hidden="true"><path d="M6.6 10.8a15.2 15.2 0 0 0 6.6 6.6l2.2-2.2a1 1 0 0 1 1-.25 11.4 11.4 0 0 0 3.6.57 1 1 0 0 1 1 1V20a1 1 0 0 1-1 1A17 17 0 0 1 3 4a1 1 0 0 1 1-1h3.5a1 1 0 0 1 1 1c0 1.25.2 2.45.57 3.6a1 1 0 0 1-.25 1z"/></svg>317.624.5583
        </span>
        <span>
          <svg viewBox="0 0 24 24" aria-hidden="true"><path d="M6 2h12v6H6z M4 9h16a2 2 0 0 1 2 2v6h-4v5H6v-5H2v-6a2 2 0 0 1 2-2z M8 15v5h8v-5z"/></svg>855.472.3308
        </span>
      </p>
      <p class="contact__line">Mark.Dolvery@brightlanecoverage.example</p>
      <p class="contact__line">www.brightlanecoverage.example</p>
    </div>
  </section>

  <section class="card card--back">
    <div class="lockup">
      <div class="lockup__dot"></div>
      <div class="lockup__name">Brightlane Coverage</div>
    </div>
  </section>

</body>
</html>
```